Website for enterprise software start-up

We need a new Wordpress website. We are an early stage start-up focused on mobile video technology for cellular operators. The audience is strategy, marketing and customer acquisition execs from the operators.

The purpose of the site is to act as a sales brochure and capture leads. A demo app can be downloaded from the current site, want to put that behind a contact form.

Current website is at www.brevlane.tv. Similar number of pages. Looking for a clean design template, with minimal customization. Blog will remain as is.

Want to be able to modify the copy via Wordpress. Reference designs I like: tarnwick.com, tessel4analytics.com

Target Market(s)

Mobile operators and MVNOs in the US and Asia Pacific regions

Industry/Entity Type

Business Software

Coding

Coded - Design and coding required

Number of Pages Required

4 page

Font styles to use
Sans Serif

Colors
f78f20

Requirements
Must have
• Form for downloading sample apps.
• Landing page with image, Product, Blog, About, Contact
• Team page

```html
<!DOCTYPE html>
<html lang="en">
<head>
<meta charset="utf-8">
<title>Brevlane Media — Mobile Video Engagement</title>
<link rel="stylesheet" href="https://fonts.googleapis.com/css2?family=Raleway:wght@300;400;600;700&family=Open+Sans:wght@400;600;700&display=swap">
<style>
:root{
  --orange:#f78f20;
  --orange-soft:#f5a65a;
  --ink:#2b2b2b;
  --text:#555;
  --muted:#999;
  --line:#e4e4e4;
  --band:#f2f2f2;
  --dark:#2e2f31;
  --dark-2:#3a3b3e;
  --white:#fff;
}
*{box-sizing:border-box;margin:0;padding:0}
html,body{width:1200px;height:4826px;overflow:hidden}
body{font-family:"Open Sans",Arial,sans-serif;color:var(--text);background:var(--white);position:relative}
.section{position:absolute;left:0;width:1200px}
.abs{position:absolute}
h1,h2,h3{font-family:"Raleway",Arial,sans-serif}
.kicker{font-family:"Raleway",Arial,sans-serif;color:var(--orange);font-size:17px;text-transform:uppercase;text-align:center;letter-spacing:.5px;width:1200px;left:0}
.section-title{font-family:"Raleway",Arial,sans-serif;font-weight:400;font-size:45px;color:var(--ink);text-align:center;width:1200px;left:0}

/* hero */
.hero{top:0;height:760px;overflow:hidden}
.hero-photo{position:absolute;inset:0;height:720px;background:linear-gradient(100deg,#cfc3b2 0%,#b8a58e 30%,#8f7a66 55%,#c9a98c 75%,#6c5a4c 100%)}
.hero-shade{position:absolute;inset:0;height:720px;background:linear-gradient(180deg,rgba(255,255,255,.15) 0%,rgba(0,0,0,.05) 60%,rgba(0,0,0,.25) 100%)}
.nav{position:absolute;top:0;left:0;width:1200px;height:100px;display:flex;align-items:center;padding:0 58px}
.brand{display:flex;align-items:center;gap:12px}
.brand-mark{width:52px;height:52px;background:var(--orange)}
.brand-name{font-family:"Raleway",Arial,sans-serif;font-weight:700;font-size:32px;color:var(--ink)}
.menu{margin-left:auto;display:flex;align-items:center;gap:6px;list-style:none}
.menu li{font-family:"Open Sans",Arial,sans-serif;font-size:15px;color:var(--ink);padding:10px 16px;text-transform:uppercase}
.menu li.active{background:var(--orange);color:var(--white)}
.menu svg{display:block}
.hero-copy{position:absolute;left:58px;top:395px;color:var(--white)}
.hero-copy h1{font-weight:600;font-size:39px;text-shadow:0 1px 3px rgba(0,0,0,.3)}
.hero-copy p{font-size:17px;line-height:24px;width:470px;margin-top:14px}
.btn{display:inline-flex;align-items:center;gap:8px;background:var(--orange);color:var(--white);font-size:16px;padding:12px 18px;margin-top:26px}
.hero-wave{position:absolute;left:0;top:600px}

/* benefits */
.benefits{top:760px;height:752px}
.feature{top:245px;width:300px}
.feature h3{font-family:"Open Sans",Arial,sans-serif;font-weight:600;font-size:18px;color:var(--ink);display:flex;align-items:center;gap:10px}
.feature h3::before{content:"";width:14px;height:14px;border:2px solid var(--orange);border-radius:50%}
.feature p{font-size:14px;line-height:20px;margin:6px 0 0 24px;color:var(--text)}
.browser{background:var(--white);border:1px solid #d9d9d9;box-shadow:0 4px 14px rgba(0,0,0,.15)}
.browser-bar{height:34px;background:#f4f4f4;border-bottom:1px solid #ddd;position:relative}
.browser-bar i{position:absolute;top:12px;width:10px;height:10px;border-radius:50%}
.video-frame{position:absolute;left:0;top:34px;right:0;bottom:0;background:linear-gradient(90deg,#8c8f95 0%,#c9c2b8 40%,#6f6b66 70%,#a49a8c 100%)}
.video-caption{position:absolute;left:0;right:0;bottom:0;height:60px;background:rgba(40,70,140,.85);color:var(--white);font-size:30px;line-height:60px;padding-left:20px;white-space:nowrap;overflow:hidden}
.phone{background:var(--white);border:2px solid #cfcfcf;border-radius:30px}

/* app band */
.app-band{top:1512px;height:129px;background:var(--orange);color:var(--white)}
.app-band p{font-size:16px}
.app-band h2{font-family:"Open Sans",Arial,sans-serif;font-weight:400;font-size:32px;margin-top:2px}
.store-badge{top:36px;height:56px;border:2px solid var(--white);border-radius:6px;background:var(--ink)}

/* push */
.push{top:1641px;height:739px}
.push h2{font-weight:400;font-size:48px;color:var(--ink)}
.push .lead{font-size:15px;line-height:22px;width:560px;color:var(--ink)}
.ticks{list-style:none}
.ticks li{display:flex;gap:14px;font-size:14px;line-height:20px;width:580px;color:var(--text);margin-bottom:20px}
.ticks li::before{content:"";flex:0 0 14px;height:14px;margin-top:3px;background:var(--orange) linear-gradient(45deg,transparent 40%,var(--white) 40%,var(--white) 55%,transparent 55%)}
.signup{left:760px;top:112px;width:366px;height:500px;border:1px solid var(--line);background:var(--white)}
.signup-head{position:absolute;left:-1px;top:-1px}
.signup-head p{position:absolute;left:0;top:28px;width:368px;text-align:center;color:var(--white);font-family:"Raleway",Arial,sans-serif;font-weight:700;font-size:17px;line-height:25px;text-transform:uppercase}
.field{position:absolute;left:40px;width:286px;height:42px;border:1px solid var(--line);font-size:13px;color:#aaa;padding:12px}
.send{position:absolute;left:40px;top:405px;width:286px;height:42px;background:var(--dark);color:var(--white);font-size:15px;text-align:center;line-height:42px}

/* blog */
.blog{top:2380px;height:708px;background:var(--band)}
.post{top:220px;width:334px;height:392px;background:var(--white)}
.post-img{height:183px}
.post .cat{font-size:12px;color:var(--muted);margin:20px 0 0 20px}
.post h3{font-family:"Open Sans",Arial,sans-serif;font-weight:700;font-size:17px;color:var(--ink);margin:8px 20px 0}
.post p{font-size:13px;line-height:20px;margin:12px 20px 0;color:var(--text)}
.meta{display:flex;align-items:center;gap:10px;font-size:11px;color:var(--ink);margin:26px 20px 0;text-transform:uppercase}
.meta i{width:18px;height:18px;background:#c9c9c9;border-radius:50%}

/* reviews */
.reviews{top:3088px;height:1030px}
.center-copy{left:0;width:1200px;text-align:center;font-size:15px;line-height:24px;color:var(--muted)}
.bubble{color:var(--white);font-size:17px;line-height:25px;padding:26px 36px}
.bubble-grey{left:135px;top:370px;width:460px;height:160px;background:#a2a2a2}
.bubble-orange{left:572px;top:404px;width:460px;height:160px;background:var(--orange-soft)}
.bubble::after{content:"";position:absolute;left:44px;bottom:-24px;border-left:0 solid transparent;border-right:28px solid transparent;border-top:24px solid}
.bubble-grey::after{border-top-color:#a2a2a2}
.bubble-orange::after{border-top-color:var(--orange-soft)}
.person{display:flex;align-items:center;gap:14px}
.person i{width:44px;height:44px;border-radius:50%;background:#bdbdbd}
.person b{display:block;font-size:17px;font-weight:600;color:var(--ink)}
.person span{font-size:13px;color:var(--muted)}
.arrow{width:44px;height:44px;border:1px solid var(--line);border-radius:50%;top:484px}
.partners{left:77px;top:694px;width:1049px;display:grid;grid-template-columns:repeat(4,1fr);border-top:1px solid var(--line);border-left:1px solid var(--line)}
.partners div{height:112px;border-right:1px solid var(--line);border-bottom:1px solid var(--line);display:flex;align-items:center;justify-content:center;font-family:"Raleway",Arial,sans-serif;font-weight:700;font-size:28px;color:#a8a8a8}
.dots{top:958px;left:0;width:1200px;display:flex;justify-content:center;gap:8px}
.dots i{width:9px;height:9px;border-radius:50%;background:#e0e0e0}
.dots i.on{background:var(--orange)}

/* footer */
.footer{top:4118px;height:708px;background:var(--dark);color:var(--white)}
.tabs{left:300px;top:70px;width:600px;display:flex;border-bottom:1px solid #555}
.tabs span{flex:1;text-align:center;font-size:14px;color:#bbb;padding-bottom:12px}
.tabs span.on{color:var(--white);border-bottom:3px solid var(--orange);margin-bottom:-2px}
.footer h2{left:0;width:1200px;text-align:center;font-weight:400;font-size:42px;top:162px}
.footer .center-copy{top:240px;color:#777}
.contact-item{top:350px;width:320px;text-align:center}
.contact-item .ring{width:92px;height:92px;border-radius:50%;background:var(--orange);margin:0 auto;display:flex;align-items:center;justify-content:center}
.contact-item b{display:block;font-size:17px;font-weight:600;margin-top:28px}
.contact-item span{display:block;font-size:13px;color:#ccc;margin-top:12px}
.socials{top:570px;left:0;width:1200px;display:flex;justify-content:center;gap:10px}
.socials i{width:30px;height:30px;border:2px solid #ccc;border-radius:50%}
.copyright{top:650px;left:0;width:1200px;text-align:center;font-size:12px;color:#999}
</style>
</head>
<body>

<header class="section hero">
  <div class="hero-photo" role="img" aria-label="Photo of a smiling man holding up a tablet outdoors at sunset"></div>
  <div class="hero-shade"></div>
  <nav class="nav">
    <div class="brand"><span class="brand-mark"></span><span class="brand-name">brevlane media</span></div>
    <ul class="menu">
      <li class="active">Home</li><li>About Us</li><li>Products</li><li>Blog</li><li>Login</li><li>Contact Us</li>
      <li><svg width="20" height="20" viewBox="0 0 20 20"><circle cx="8" cy="8" r="6" fill="none" stroke="#2b2b2b" stroke-width="2.5"/><line x1="12.5" y1="12.5" x2="18" y2="18" stroke="#2b2b2b" stroke-width="2.5"/></svg></li>
      <li><svg width="20" height="20" viewBox="0 0 20 20"><circle cx="10" cy="6" r="4.5" fill="#2b2b2b"/><path d="M2 19c0-5 4-7 8-7s8 2 8 7z" fill="#2b2b2b"/></svg></li>
    </ul>
  </nav>
  <div class="hero-copy">
    <h1>High Quality Mobile Engagement</h1>
    <p>We engage mobile audiences with the right video content at the perfect moment.</p>
    <span class="btn"><svg width="14" height="14" viewBox="0 0 14 14"><path d="M7 1l1.8 4 4.2.4-3.2 2.8 1 4.2L7 10.2 3.2 12.4l1-4.2L1 5.4l4.2-.4z" fill="none" stroke="#fff" stroke-width="1.3"/></svg>Sample Apps</span>
  </div>
  <svg class="hero-wave" width="1200" height="160" viewBox="0 0 1200 160">
    <path d="M0 160V110C300 140 500 150 620 140C800 125 1000 80 1200 70V160z" fill="#fff"/>
    <polyline points="0,95 120,80 260,140 400,120 580,100 745,100 880,90 1000,62 1110,90 1200,70" fill="none" stroke="#f78f20" stroke-width="3"/>
    <g fill="#fff" stroke="#f78f20" stroke-width="2">
      <circle cx="120" cy="80" r="6"/><circle cx="260" cy="140" r="6"/><circle cx="400" cy="120" r="6"/><circle cx="580" cy="100" r="6"/><circle cx="745" cy="100" r="6"/><circle cx="880" cy="90" r="6"/><circle cx="1000" cy="62" r="6"/><circle cx="1110" cy="90" r="6"/>
    </g>
  </svg>
</header>

<section class="section benefits">
  <p class="abs kicker" style="top:62px">About Product</p>
  <h2 class="abs section-title" style="top:92px">Interface Benefits</h2>

  <div class="abs feature" style="left:80px"><h3>Secure Login</h3><p>Lorem ipsum dolor sit amet, consectetur adipiscing elit</p></div>
  <div class="abs feature" style="left:470px"><h3>Easy Accessible</h3><p>Lorem ipsum dolor sit amet, consectetur adipiscing elit</p></div>
  <div class="abs feature" style="left:850px"><h3>Quick Results</h3><p>Lorem ipsum dolor sit amet, consectetur adipiscing elit</p></div>

  <div class="abs browser" style="left:880px;top:445px;width:262px;height:310px">
    <div class="browser-bar"></div>
    <div style="position:absolute;left:24px;top:80px;display:flex;align-items:center;gap:8px"><span style="width:30px;height:30px;background:var(--orange)"></span><span style="font-family:'Raleway',Arial,sans-serif;font-weight:700;font-size:26px;color:var(--ink)">brevlane media</span></div>
  </div>
  <div class="abs browser" style="left:155px;top:378px;width:740px;height:380px">
    <div class="browser-bar"><i style="left:14px;background:#ee5b52"></i><i style="left:30px;background:#f5bd3b"></i><i style="left:46px;background:#5fc451"></i></div>
    <div class="video-frame" role="img" aria-label="Video still of two men talking in an office">
      <div class="video-caption">is driving growth in video consumption</div>
    </div>
  </div>
  <div class="abs phone" style="left:58px;top:528px;width:200px;height:300px">
    <div style="position:absolute;left:14px;top:40px;width:168px;height:150px;background:#f6f6f6;border:1px solid #ddd;padding:10px;font-size:9px;line-height:12px;color:var(--ink)">
      <div style="display:flex;gap:6px;align-items:center"><span style="width:16px;height:16px;background:var(--orange)"></span><b>Welcome to the Push Video Showcase App</b></div>
      <p style="margin-top:8px">Please sign in to unlock the demo videos.</p>
      <div style="height:14px;border:1px solid #ccc;background:#fff;margin-top:6px"></div>
      <div style="height:14px;border:1px solid #ccc;background:#fff;margin-top:4px"></div>
      <div style="height:14px;background:#444;margin-top:6px"></div>
    </div>
  </div>
</section>

<section class="section app-band">
  <div class="abs" style="left:58px;top:26px">
    <p>Personalised flawless HD videos, discoverable in-app, and playable even when offline</p>
    <h2>DOWNLOAD SAMPLE APP HERE</h2>
  </div>
  <div class="abs store-badge" style="left:814px;width:148px"></div>
  <div class="abs store-badge" style="left:982px;width:160px"></div>
</section>

<section class="section push">
  <h2 class="abs" style="left:58px;top:124px">Native Push Video</h2>
  <p class="abs lead" style="left:58px;top:196px">Personalised flawless HD videos, revealed at the perfect moment, as rich media notifications.</p>
  <ul class="abs ticks" style="left:58px;top:270px">
    <li>Reach your mobile audience with beautiful HD thumbnails and in-notification videos.</li>
    <li>Instant video playback, zero buffering, guaranteed flawless playback - even when offline.</li>
    <li>Content is personalised based on viewer interests and mobile viewing habits.</li>
    <li>Monetize with beautiful HD preroll or interstitial ads.</li>
    <li>Easily added to your existing apps within one hour.</li>
  </ul>
  <div class="abs signup">
    <div class="signup-head">
      <svg width="368" height="150" viewBox="0 0 368 150"><path d="M0 0H368V112Q184 170 0 112z" fill="#f78f20"/></svg>
      <p>Create your free account now<br>and get immediate access<br>to our app</p>
    </div>
    <div class="field" style="top:184px">Name</div>
    <div class="field" style="top:238px">Email</div>
    <div class="field" style="top:292px">Subject</div>
    <div class="field" style="top:346px;height:48px">Message</div>
    <div class="send">Send Message</div>
  </div>
</section>

<section class="section blog">
  <p class="abs kicker" style="top:90px">From the Blog</p>
  <h2 class="abs section-title" style="top:118px">We share useful blog posts</h2>

  <article class="abs post" style="left:58px">
    <div class="post-img" role="img" aria-label="Desk with books, a coffee cup and a screen about e-learning" style="background:linear-gradient(135deg,#8fb7d6,#d9c6a8 60%,#6a7c8c)"></div>
    <p class="cat">Web Design</p><h3>E-Learning System For Everything</h3>
    <p>Lorem Ipsum is simply dummy text of the printing and typesetting industry.</p>
    <div class="meta"><i></i>Amanda Doe &nbsp;| 12 March 2016 &nbsp;| 12 Comments</div>
  </article>
  <article class="abs post" style="left:434px">
    <div class="post-img" role="img" aria-label="Books, an apple and pencils in front of a chalkboard" style="background:linear-gradient(135deg,#3f4744,#5c665f 50%,#b5884d)"></div>
    <p class="cat">Web Design</p><h3>Way To Learn Than To Go To School</h3>
    <p>Lorem Ipsum is simply dummy text of the printing and typesetting industry.</p>
    <div class="meta"><i></i>Jenny Doe &nbsp;| 11 March 2016 &nbsp;| 78 Comments</div>
  </article>
  <article class="abs post" style="left:807px">
    <div class="post-img" role="img" aria-label="Group of students working together at laptops" style="background:linear-gradient(135deg,#e2ddd6,#b7a08a 50%,#6f7d8f)"></div>
    <p class="cat">Web Design</p><h3>The Benefits Of Teamwork</h3>
    <p>Lorem Ipsum is simply dummy text of the printing and typesetting industry.</p>
    <div class="meta"><i></i>Amanda Doe &nbsp;| 09 March 2016 &nbsp;| 23 Comments</div>
  </article>
</section>

<section class="section reviews">
  <p class="abs kicker" style="top:100px">About Reviews</p>
  <h2 class="abs section-title" style="top:128px">What Clients Say?</h2>
  <p class="abs center-copy" style="top:222px">Sed condimentum ante ac quam varius pretium. Nunc ornare laoreet augue et elementum.<br>Phasellus libero, blandit vel sapien vitae, condimentum ultricies magna et.</p>

  <span class="abs arrow" style="left:26px"></span>
  <span class="abs arrow" style="left:1130px"></span>

  <div class="abs bubble bubble-grey">Sed condimentum ante ac quam varius pretium. Nunc ornare laoreet augue et elementum. Phasellus libero.</div>
  <div class="abs person" style="left:160px;top:556px"><i></i><div><b>John Doe</b><span>Web designer</span></div></div>
  <div class="abs bubble bubble-orange" style="padding-left:86px">Lorem ipsum dolor sit amet, consectetur adipiscing elit. Enim, dolectus aliqu nidit esse harum! Saepe!</div>
  <div class="abs person" style="left:594px;top:586px"><i></i><div><b>Jessica Doe</b><span>Developer</span></div></div>

  <div class="abs partners">
    <div>Lumenvia</div><div>CORVALE</div><div>Quillora</div><div style="font-size:20px">Halden Sound Group</div>
    <div>Northwire TV</div><div>Stratton Arena</div><div>PELLUCID</div><div>Riverhawks</div>
  </div>
  <div class="abs dots"><i class="on"></i><i></i><i></i><i></i><i></i></div>
</section>

<footer class="section footer">
  <div class="abs tabs"><span class="on">Contact Info</span><span>Service Inquiry</span><span>View on Map</span></div>
  <h2 class="abs">Contact Info</h2>
  <p class="abs center-copy">Sed condimentum ante ac quam varius pretium. Nunc ornare laoreet augue et elementum.<br>Phasellus enim libero, blandit vel sapien vitae, condimentum ultricies magna et.</p>

  <div class="abs contact-item" style="left:100px">
    <div class="ring"><svg width="30" height="30" viewBox="0 0 30 30"><path d="M15 3a9 9 0 0 0-9 9c0 7 9 15 9 15s9-8 9-15a9 9 0 0 0-9-9z" fill="none" stroke="#fff" stroke-width="2.2"/><circle cx="15" cy="12" r="3.2" fill="none" stroke="#fff" stroke-width="2.2"/></svg></div>
    <b>Address</b><span>48 Alder Row, Kestrel Bay, 204815</span>
  </div>
  <div class="abs contact-item" style="left:440px">
    <div class="ring"><svg width="30" height="30" viewBox="0 0 30 30"><path d="M8 4l5 5-3 3c1.5 3.5 4.5 6.5 8 8l3-3 5 5-3 4C12 26 4 18 4 7z" fill="none" stroke="#fff" stroke-width="2.2" stroke-linejoin="round"/></svg></div>
    <b>Phones</b><span>+1 555 204 18 63, +1 555 204 18 64</span>
  </div>
  <div class="abs contact-item" style="left:780px">
    <div class="ring"><svg width="32" height="24" viewBox="0 0 32 24"><rect x="2" y="2" width="28" height="20" fill="none" stroke="#fff" stroke-width="2.2"/><path d="M2 3l14 11L30 3" fill="none" stroke="#fff" stroke-width="2.2"/></svg></div>
    <b>E-mail</b><span>info@brevlane.tv, support@brevlane.tv</span>
  </div>

  <div class="abs socials"><i></i><i></i><i></i></div>
  <p class="abs copyright">© 2016 Brevlane Media, Inc. · Privacy Policy</p>
</footer>

</body>
</html>
```